Salad Dressing label for gourmet food business.

We have been producing condiments from traditional recipes for over 50 years. It's time for the Salad Dressing range to have an overhaul. Each one of our ranges (Mustard, Simmer Sauce, Jam, Chocolate Sauce etc) has a unique bottle and label but we would like our branding to be identified across the entire range. We mainly sell to delicatessens, gift stores, hamper businesses, gourmet food stores, tourism destinations, cafes.
www.brindlewoodpantry.com.au
Target Market(s)
Gourmet food stores, deli, hampers, gift stores
Requirements
Must have
- Label design to fit 250ml dorica bottle.
Foil - Perhaps in border or logo
This is a range of 10 dressings and expanding. Product name, ingredients, NIPS and COO's, the barcode will be overprinted on a thermal printer.
Nice to have
- Serving suggestions
Have elements that tie in with our lines.
Salad Dressings (tall bottle) as per photos attached
We like the Sample Dressings photo attached, Spiced Pear and Ginger. We like the silver foil (but we would like gold) border and in the picture on the label. Perhaps the logo could go here with gold foil? I don't mind the green as it represents fresh salad.
We would like the finished product to represent established quality and authenticity. Product cooked from traditional recipes but would like the look to be relevant to modern times with an interesting, delicious must-try look.
Should not have
- Should not look like a supermarket product.

```html
<!DOCTYPE html>
<html lang="en">
<head>
<meta charset="utf-8">
<title>Brindlewood Pantry – Salted Caramel Sauce Label</title>
<link href="https://fonts.googleapis.com/css2?family=Cinzel:wght@500;600;700&family=Roboto+Condensed:wght@500&family=Open+Sans:wght@600&display=swap" rel="stylesheet">
<style>
  :root {
    --backdrop: #d6d7d9;
    --cream-light: #fbf3da;
    --cream-deep: #efdcaa;
    --maroon: #6b1a14;
    --green: #1f7a45;
    --green-dark: #145c32;
    --gold: #c9a24a;
    --ink: #222222;
    --white: #ffffff;
  }
  * { margin: 0; padding: 0; box-sizing: border-box; }
  html, body { width: 1200px; height: 1200px; overflow: hidden; }
  body {
    background: var(--backdrop);
    position: relative;
  }
  .label {
    position: absolute;
    left: 300px;
    top: 200px;
    width: 600px;
    height: 800px;
    background: radial-gradient(ellipse at 50% 45%, var(--cream-light) 0%, var(--cream-light) 45%, var(--cream-deep) 100%);
    overflow: hidden;
  }
  .ornament-band {
    position: absolute;
    left: 0;
    width: 100%;
    height: 34px;
    background: var(--green);
    border-top: 3px solid var(--gold);
    border-bottom: 3px solid var(--gold);
  }
  .ornament-band--top { top: 0; }
  .ornament-band--bottom { top: 730px; }
  .brand {
    position: absolute;
    top: 90px;
    left: 0;
    width: 100%;
    text-align: center;
  }
  .brand__dot {
    display: block;
    width: 26px;
    height: 26px;
    margin: 0 auto 16px;
    border-radius: 50%;
    background: var(--gold);
  }
  .brand__name {
    font-family: 'Cinzel', serif;
    font-weight: 700;
    font-size: 30px;
    letter-spacing: 8px;
    line-height: 1.25;
    color: var(--ink);
  }
  .product {
    position: absolute;
    top: 300px;
    left: 0;
    width: 100%;
    text-align: center;
    color: var(--maroon);
    font-family: 'Cinzel', serif;
    font-weight: 600;
  }
  .product__flavour {
    font-size: 58px;
    line-height: 1.1;
    letter-spacing: 1px;
  }
  .product__type {
    display: flex;
    align-items: center;
    justify-content: center;
    gap: 20px;
    font-size: 56px;
    line-height: 1.2;
    margin-top: 8px;
  }
  .product__rule {
    width: 90px;
    height: 2px;
    background: var(--maroon);
    opacity: 0.7;
  }
  .product__tagline {
    display: inline-block;
    margin-top: 20px;
    padding: 6px 24px;
    border-radius: 30px;
    background: linear-gradient(var(--green), var(--green-dark));
    color: var(--cream-light);
    font-size: 28px;
    font-weight: 500;
    letter-spacing: 1px;
  }
  .net-volume {
    position: absolute;
    top: 598px;
    left: 0;
    width: 100%;
    text-align: center;
    font-family: 'Roboto Condensed', sans-serif;
    font-weight: 500;
    font-size: 34px;
    color: var(--ink);
  }
  .origin-banner {
    position: absolute;
    top: 682px;
    left: 0;
    width: 100%;
    height: 48px;
    background: var(--white);
    border-top: 3px solid #3a3a3a;
    clip-path: polygon(3% 0, 97% 0, 100% 100%, 0 100%);
    display: flex;
    align-items: center;
    justify-content: center;
    font-family: 'Open Sans', sans-serif;
    font-weight: 600;
    font-size: 20px;
    color: var(--ink);
  }
</style>
</head>
<body>
  <div class="label">
    <div class="ornament-band ornament-band--top" role="img" aria-label="Green band with gold fleur-de-lis pattern"></div>

    <div class="brand">
      <span class="brand__dot"></span>
      <div class="brand__name">BRINDLEWOOD<br>PANTRY</div>
    </div>

    <div class="product">
      <div class="product__flavour">Salted Caramel</div>
      <div class="product__type">
        <span class="product__rule"></span>
        <span>Sauce</span>
        <span class="product__rule"></span>
      </div>
      <div class="product__tagline">Rich &amp; Flavoursome</div>
    </div>

    <div class="net-volume">Net - 250ml</div>

    <div class="origin-banner">PROUDLY AUSTRALIAN OWNED &amp; MADE</div>
    <div class="ornament-band ornament-band--bottom" role="img" aria-label="Green band with gold fleur-de-lis pattern"></div>
  </div>
</body>
</html>
```